Menu Edit

Hello. We need a pricing edit on our current menu and new logo swapped (we already have the new logo), as well as colour changes. Also, we require a takeaway menu, in-store menu and footpath a-frame edit as well. I have attached the files bellow.

```html
<!DOCTYPE html>
<html lang="en">
<head>
<meta charset="utf-8">
<title>Tide &amp; Ember Fish Grill – Menu Board Options</title>
<link rel="stylesheet" href="https://fonts.googleapis.com/css2?family=Montserrat:wght@400;500;600;700&family=Roboto+Slab:wght@700&display=swap">
<style>
  :root {
    --page: #e1e2e1;
    --ink: #0c0c0d;
    --ink-deep: #050506;
    --paper: #ffffff;
    --flame: #e8442a;
    --navy: #1d2046;
    --caption: #222222;
  }
  * { box-sizing: border-box; margin: 0; padding: 0; }
  html, body { width: 897px; height: 1200px; overflow: hidden; background: var(--page); }
  .sheet {
    position: absolute; left: 0; top: 0;
    width: 1654px; height: 2212px;
    transform: scale(0.54232); transform-origin: 0 0;
    font-family: "Montserrat", Arial, sans-serif;
  }
  .board {
    position: absolute; width: 619px; height: 917px; overflow: hidden;
  }
  .board--dark { background: var(--ink); color: var(--paper); }
  .board--light { background: var(--paper); color: var(--ink); }
  .board--tl { left: 191px; top: 86px; }
  .board--tr { left: 844px; top: 86px; }
  .board--bl { left: 191px; top: 1027px; }
  .board--br { left: 844px; top: 1027px; }

  .row {
    position: absolute; left: 0; right: 0;
    text-align: center; white-space: nowrap;
    transform: translateY(-50%);
  }
  .rule { position: absolute; height: 2px; background: var(--flame); }
  .rule--wide { left: 49px; right: 49px; }
  .rule--list { left: 41px; right: 41px; }

  .brand-box {
    position: absolute; left: 110px; top: 65px; width: 399px; height: 134px;
    background: var(--ink-deep);
  }
  .brand {
    font-weight: 600; font-size: 29px; letter-spacing: 0.5px;
    display: flex; justify-content: center; align-items: center; gap: 14px;
  }
  .brand-mark { width: 22px; height: 22px; background: var(--flame); flex: none; }
  .board--dark .brand { color: var(--paper); }

  .title {
    font-family: "Roboto Slab", Georgia, serif; font-weight: 700;
    color: var(--flame);
  }
  .title--hours { font-size: 57px; }
  .title--platters { font-size: 45px; }

  .hours { font-size: 27px; font-weight: 500; }
  .hours b { font-weight: 700; margin-right: 14px; }
  .service { font-size: 28px; font-weight: 500; letter-spacing: 0.6px; }
  .byo { font-size: 18.5px; font-weight: 600; }
  .prep-label { font-size: 23px; font-weight: 500; }
  .prep-options { font-size: 20px; font-weight: 500; }

  .platter { font-size: 24px; font-weight: 700; letter-spacing: 0.4px; }
  .includes-label { font-size: 21px; font-weight: 700; }
  .includes { font-size: 22px; line-height: 30px; font-weight: 400; white-space: normal; }

  .phone-bar {
    position: absolute; left: 6px; right: 6px; top: 720px; height: 88px;
    background: var(--flame); color: var(--paper);
    display: flex; align-items: center; justify-content: center; gap: 16px;
    font-weight: 700; font-size: 68px; letter-spacing: 1px;
  }
  .phone-bar svg { width: 62px; height: 50px; flex: none; }
  .web-bar {
    position: absolute; left: 6px; right: 6px; top: 819px; height: 47px;
    display: flex; align-items: center; justify-content: center;
    font-weight: 700; font-size: 27px; letter-spacing: 0.3px;
  }
  .board--dark .web-bar { background: var(--paper); color: var(--navy); }
  .board--light .web-bar { background: var(--ink); color: var(--paper); }

  .caption {
    position: absolute; left: 0; right: 0; top: 1993px;
    text-align: center; color: var(--caption);
    font-family: "Roboto Slab", Georgia, serif; font-weight: 700;
    font-size: 44px; line-height: 50px;
  }
</style>
</head>
<body>
<svg width="0" height="0" style="position:absolute" aria-hidden="true">
  <symbol id="icon-phone" viewBox="0 0 62 50">
    <path fill="currentColor" d="M2 16C2 8 12 3 31 3s29 5 29 13v5c0 2-1 3-3 3h-9c-2 0-3-1-3-3v-5c-4-1-9-1-14-1s-10 0-14 1v5c0 2-1 3-3 3H5c-2 0-3-1-3-3z"/>
    <path fill="currentColor" d="M19 20h24l12 16v10c0 2-1 3-3 3H10c-2 0-3-1-3-3V36z"/>
    <g fill="#e8442a">
      <rect x="23" y="28" width="4" height="3"/><rect x="29" y="28" width="4" height="3"/><rect x="35" y="28" width="4" height="3"/>
      <rect x="23" y="34" width="4" height="3"/><rect x="29" y="34" width="4" height="3"/><rect x="35" y="34" width="4" height="3"/>
      <rect x="23" y="40" width="4" height="3"/><rect x="29" y="40" width="4" height="3"/><rect x="35" y="40" width="4" height="3"/>
    </g>
  </symbol>
</svg>

<main class="sheet">

  <!-- Opening hours board, dark -->
  <section class="board board--dark board--tl">
    <div class="brand-box"></div>
    <div class="row brand" style="top:172px"><span>TIDE &amp; EMBER FISH GRILL</span><span class="brand-mark"></span></div>
    <h2 class="row title title--hours" style="top:282px">Open Every Day</h2>
    <p class="row hours" style="top:350px"><b>Mon – Thurs</b>5pm to 9pm</p>
    <p class="row hours" style="top:384px"><b>Fri – Sun</b>12pm to 9pm</p>
    <div class="rule rule--wide" style="top:429px"></div>
    <p class="row service" style="top:460px">CASUAL DINING | TAKEAWAY</p>
    <p class="row service" style="top:495px">ONLINE ORDERING &amp; DELIVERY</p>
    <p class="row service" style="top:530px">FRESH RETAIL</p>
    <p class="row byo" style="top:569px">BYO Welcome! Wine, Beer &amp; Spirits / Soft Drinks Available</p>
    <div class="rule rule--wide" style="top:595px"></div>
    <p class="row prep-label" style="top:637px">Choose your preparation:</p>
    <p class="row prep-options" style="top:667px">PANKO CRUMBED / TEMPURA BATTERED / GRILLED</p>
    <div class="rule rule--wide" style="top:688px"></div>
    <div class="phone-bar"><svg><use href="#icon-phone"/></svg><span>3555 0142</span></div>
    <div class="web-bar">www.tideandember.com.au</div>
  </section>

  <!-- Seafood platters board, dark -->
  <section class="board board--dark board--tr">
    <div class="brand-box"></div>
    <div class="row brand" style="top:172px"><span>TIDE &amp; EMBER FISH GRILL</span><span class="brand-mark"></span></div>
    <h2 class="row title title--platters" style="top:278px">Cooked Seafood Platters</h2>
    <p class="row platter" style="top:364px">Cooked Platter for One</p>
    <div class="rule rule--list" style="top:385px"></div>
    <p class="row platter" style="top:411px">Cooked Platter for Two</p>
    <div class="rule rule--list" style="top:432px"></div>
    <p class="row platter" style="top:458px">Cooked Platter for Three</p>
    <div class="rule rule--list" style="top:479px"></div>
    <p class="row includes-label" style="top:542px">Cooked Seafood Platters include:</p>
    <p class="row includes" style="top:623px">Queensland whiting, calamari, salt &amp; pepper<br>calamari, ocean king prawns, sea scallops, beer<br>battered chips, one of our freshly made salads,<br>homemade tartare sauce, lemon &amp; parsley.</p>
    <div class="phone-bar"><svg><use href="#icon-phone"/></svg><span>3555 0142</span></div>
    <div class="web-bar">www.tideandember.com.au</div>
  </section>

  <!-- Opening hours board, light -->
  <section class="board board--light board--bl">
    <div class="row brand" style="top:170px"><span>TIDE &amp; EMBER FISH GRILL</span><span class="brand-mark"></span></div>
    <h2 class="row title title--hours" style="top:282px">Open Every Day</h2>
    <p class="row hours" style="top:350px"><b>Mon – Thurs</b>5pm to 9pm</p>
    <p class="row hours" style="top:384px"><b>Fri – Sun</b>12pm to 9pm</p>
    <div class="rule rule--wide" style="top:429px"></div>
    <p class="row service" style="top:460px">CASUAL DINING | TAKEAWAY</p>
    <p class="row service" style="top:495px">ONLINE ORDERING &amp; DELIVERY</p>
    <p class="row service" style="top:530px">FRESH RETAIL</p>
    <p class="row byo" style="top:569px">BYO Welcome! Wine, Beer &amp; Spirits / Soft Drinks Available</p>
    <div class="rule rule--wide" style="top:595px"></div>
    <p class="row prep-label" style="top:637px">Choose your preparation:</p>
    <p class="row prep-options" style="top:667px">PANKO CRUMBED / TEMPURA BATTERED / GRILLED</p>
    <div class="rule rule--wide" style="top:688px"></div>
    <div class="phone-bar"><svg><use href="#icon-phone"/></svg><span>3555 0142</span></div>
    <div class="web-bar">www.tideandember.com.au</div>
  </section>

  <!-- Seafood platters board, light -->
  <section class="board board--light board--br">
    <div class="row brand" style="top:170px"><span>TIDE &amp; EMBER FISH GRILL</span><span class="brand-mark"></span></div>
    <h2 class="row title title--platters" style="top:278px">Cooked Seafood Platters</h2>
    <p class="row platter" style="top:364px">Cooked Platter for One</p>
    <div class="rule rule--list" style="top:385px"></div>
    <p class="row platter" style="top:411px">Cooked Platter for Two</p>
    <div class="rule rule--list" style="top:432px"></div>
    <p class="row platter" style="top:458px">Cooked Platter for Three</p>
    <div class="rule rule--list" style="top:479px"></div>
    <p class="row includes-label" style="top:542px">Cooked Seafood Platters include:</p>
    <p class="row includes" style="top:623px">Queensland whiting, calamari, salt &amp; pepper<br>calamari, ocean king prawns, sea scallops, beer<br>battered chips, one of our freshly made salads,<br>homemade tartare sauce, lemon &amp; parsley.</p>
    <div class="phone-bar"><svg><use href="#icon-phone"/></svg><span>3555 0142</span></div>
    <div class="web-bar">www.tideandember.com.au</div>
  </section>

  <p class="caption">Here is the first menu (Black and White versions)<br>Let me know if you like any of these<br>versions to continue the other 2 menus</p>

</main>
</body>
</html>
```